Business Card Design

I need a business card design for my law office based in Pasadena, California. I am a sole practitioner and I specialize in business transaction and litigation, probate and estate planning, taxation law, corporate and business formation, immigration and real estate. I want something that is simple, yet stands out.

A friend helped to create a logo about 6 years ago. I am open to new ideas to changing the logo.

Industry/Entity Type

Business

Contact Information for Business Card

Law Offices of Dorvan L. Mabry
842 W. Larkspur Ave., Suite 319
Pasadena, CA 90287
Tel: 626-555-0174
Fax: 626-555-0139
Email: dmabry@dlmlegalgroup.example

Attorney: Dorvan L. Mabry

```html
<!DOCTYPE html>
<html lang="en">
<head>
<meta charset="utf-8">
<title>Business Card — Law Offices of Dorvan L. Mabry</title>
<link rel="stylesheet" href="https://fonts.googleapis.com/css2?family=Cinzel:wght@400;500&family=Open+Sans:wght@400;600&display=swap">
<style>
  :root {
    --backdrop: #4a3e39;
    --card-black: #161616;
    --card-edge: #222;
    --ink-white: #f1f1f1;
    --ink-soft: #cfcfcf;
    --ink-muted: #9a9a9a;
    --gloss: #2c2c2c;
    --rule: #8c8c8c;
  }
  * { box-sizing: border-box; margin: 0; padding: 0; }
  html, body {
    width: 1200px; height: 716px; overflow: hidden;
    background: var(--backdrop);
  }
  .canvas {
    position: relative; width: 1200px; height: 716px;
    display: flex; align-items: center; justify-content: center; gap: 50px;
  }
  .card {
    position: relative; width: 525px; height: 300px;
    background: var(--card-black);
    border: 1px solid var(--card-edge);
    border-radius: 3px;
    box-shadow: 0 12px 30px rgba(0,0,0,.45);
  }
  /* back of card */
  .card-back { display: flex; align-items: center; justify-content: center; }
  .brand-mark {
    display: flex; align-items: center; gap: 14px;
    font-family: "Cinzel", serif; font-weight: 400;
    font-size: 34px; letter-spacing: 3px; color: var(--gloss);
  }
  .brand-square { width: 22px; height: 22px; background: var(--gloss); }

  /* front of card */
  .card-front { display: flex; }
  .identity {
    width: 50%; display: flex; flex-direction: column;
    align-items: center; justify-content: center; padding-top: 6px;
  }
  .identity .brand-mark { font-size: 20px; letter-spacing: 2px; color: var(--ink-white); gap: 10px; margin-bottom: 22px; }
  .identity .brand-square { width: 13px; height: 13px; background: var(--ink-white); }
  .firm-label {
    font-family: "Cinzel", serif; font-size: 8px; letter-spacing: 3px;
    color: var(--ink-soft); text-transform: uppercase;
  }
  .firm-name {
    font-family: "Cinzel", serif; font-size: 25px; letter-spacing: 1px;
    color: var(--ink-white); margin-top: 2px; padding-bottom: 6px;
    border-bottom: 1px solid var(--rule);
  }
  .details { width: 50%; padding: 86px 20px 0 10px; }
  .attorney-name {
    font-family: "Cinzel", serif; font-size: 20px; color: var(--ink-white); line-height: 1;
  }
  .attorney-title {
    font-family: "Open Sans", sans-serif; font-size: 10px; color: var(--ink-soft); margin: 3px 0 14px;
  }
  .contact-list { list-style: none; font-family: "Open Sans", sans-serif; font-size: 10.5px; color: var(--ink-white); }
  .contact-list li { display: flex; align-items: flex-start; gap: 8px; line-height: 1.45; }
  .contact-list svg { width: 10px; height: 10px; margin-top: 3px; flex: none; fill: var(--ink-muted); }
</style>
</head>
<body>
<main class="canvas">
  <section class="card card-back" aria-label="Card back">
    <div class="brand-mark"><span class="brand-square"></span>Mabry Law</div>
  </section>

  <section class="card card-front" aria-label="Card front">
    <div class="identity">
      <div class="brand-mark"><span class="brand-square"></span>Mabry Law</div>
      <p class="firm-label">Law Offices of</p>
      <h1 class="firm-name">Dorvan L. Mabry</h1>
    </div>
    <div class="details">
      <h2 class="attorney-name">Dorvan L. Mabry</h2>
      <p class="attorney-title">Attorney / Lawyer</p>
      <ul class="contact-list">
        <li><svg viewBox="0 0 10 10"><path d="M2 0h2l1 2.5-1.3 1a5 5 0 0 0 2.8 2.8l1-1.3L10 6v2a2 2 0 0 1-2 2A8 8 0 0 1 0 2a2 2 0 0 1 2-2z"/></svg>626-555-0174</li>
        <li><svg viewBox="0 0 10 10"><path d="M2 0h6v3H2zM0 3.5h10v5H8V7H2v1.5H0zM2.5 7.5h5V10h-5z"/></svg>626-555-0139</li>
        <li><svg viewBox="0 0 10 10"><path d="M0 2h10v6H0zM0.8 2.6 5 5.6l4.2-3z" fill-rule="evenodd"/></svg>dmabry@dlmlegalgroup.example</li>
        <li><svg viewBox="0 0 10 10"><path d="M5 0a3.5 3.5 0 0 1 3.5 3.5C8.5 6 5 10 5 10S1.5 6 1.5 3.5A3.5 3.5 0 0 1 5 0zm0 2a1.5 1.5 0 1 0 0 3 1.5 1.5 0 0 0 0-3z" fill-rule="evenodd"/></svg>842 W. Larkspur Ave., Suite 319<br>Pasadena, CA 90287</li>
        <li><svg viewBox="0 0 10 10"><path d="M5 0a5 5 0 1 1 0 10A5 5 0 0 1 5 0zm0 1.5a3.5 3.5 0 1 0 0 7 3.5 3.5 0 0 0 0-7zM5 3a2 2 0 1 1 0 4 2 2 0 0 1 0-4z" fill-rule="evenodd"/></svg>www.dlmlegalgroup.example</li>
      </ul>
    </div>
  </section>
</main>
</body>
</html>
```